Sunridge Lighting Distributors Business Card Design

Use logo and expand the framing box to the extents of the business card. Keep company name in right bottom corner and triangle at top right corner. I would like to have a template so that I can fill in employee name, contact info, email and website.

```html
<!DOCTYPE html>
<html lang="en">
<head>
<meta charset="utf-8">
<title>Sunridge Lighting Distributors – Business Card</title>
<link href="https://fonts.googleapis.com/css2?family=Montserrat:wght@400;700&display=swap" rel="stylesheet">
<style>
  :root {
    --backdrop: #0b86c8;
    --brand-blue: #0b84c6;
    --navy: #011e2b;
    --navy-line: #13202d;
    --white: #ffffff;
    --grey-text: #3a3a3a;
    --ink: #1b1b1b;
  }
  html, body {
    margin: 0;
    padding: 0;
    width: 1200px;
    height: 1200px;
    overflow: hidden;
    background: var(--backdrop);
  }
  .canvas {
    position: relative;
    width: 1200px;
    height: 1200px;
  }
  .card {
    position: absolute;
    left: 180px;
    width: 840px;
    height: 480px;
    overflow: hidden;
    box-shadow: 0 6px 18px rgba(0, 0, 0, 0.25);
  }
  .card--front { top: 80px; background: var(--white); }
  .card--back  { top: 640px; background: var(--navy); }
  .card__frame {
    position: absolute;
    inset: 0;
    width: 840px;
    height: 480px;
  }
  .contact-block {
    position: absolute;
    left: 62px;
    top: 318px;
    font-family: "Montserrat", sans-serif;
  }
  .contact-block__name {
    margin: 0;
    font-size: 34px;
    font-weight: 700;
    letter-spacing: 0.5px;
    line-height: 1;
    color: var(--brand-blue);
  }
  .contact-block__position {
    margin: 4px 0 10px;
    font-size: 16px;
    font-weight: 400;
    letter-spacing: 1px;
    color: var(--grey-text);
  }
  .contact-list {
    list-style: none;
    margin: 0;
    padding: 0;
  }
  .contact-list__item {
    display: flex;
    align-items: center;
    gap: 10px;
    height: 26px;
    font-size: 18px;
    color: var(--ink);
  }
  .contact-list__icon {
    width: 20px;
    height: 20px;
    flex: none;
  }
  .company-name {
    position: absolute;
    left: 62px;
    top: 330px;
    width: 420px;
    margin: 0;
    font-family: "Montserrat", sans-serif;
    font-weight: 700;
    font-size: 38px;
    line-height: 1.15;
    color: var(--white);
  }
</style>
</head>
<body>
<main class="canvas">

  <section class="card card--front" aria-label="Business card front">
    <svg class="card__frame" viewBox="0 0 840 480" aria-hidden="true">
      <polygon points="440,54 800,40 800,162" fill="var(--brand-blue)"/>
      <rect x="40" y="40" width="380" height="18" fill="var(--navy-line)"/>
      <rect x="40" y="40" width="18" height="262" fill="var(--navy-line)"/>
      <rect x="782" y="180" width="18" height="260" fill="var(--navy-line)"/>
      <rect x="400" y="422" width="400" height="18" fill="var(--navy-line)"/>
    </svg>

    <div class="contact-block">
      <h1 class="contact-block__name">FULL NAME</h1>
      <p class="contact-block__position">POSITION</p>
      <ul class="contact-list">
        <li class="contact-list__item">
          <svg class="contact-list__icon" viewBox="0 0 24 24" aria-hidden="true">
            <path fill="var(--brand-blue)" d="M6.6 10.8a15.1 15.1 0 0 0 6.6 6.6l2.2-2.2a1 1 0 0 1 1-.25 11.4 11.4 0 0 0 3.6.57 1 1 0 0 1 1 1V20a1 1 0 0 1-1 1A17 17 0 0 1 3 4a1 1 0 0 1 1-1h3.5a1 1 0 0 1 1 1c0 1.25.2 2.45.57 3.57a1 1 0 0 1-.25 1z"/>
          </svg>
          (000) 000 0000
        </li>
        <li class="contact-list__item">
          <svg class="contact-list__icon" viewBox="0 0 24 24" aria-hidden="true">
            <rect x="2" y="5" width="20" height="14" fill="var(--brand-blue)"/>
            <path d="M2 5l10 8 10-8M2 19l7-7M22 19l-7-7" stroke="var(--white)" stroke-width="1.6" fill="none"/>
          </svg>
          email@company.com
        </li>
        <li class="contact-list__item">
          <svg class="contact-list__icon" viewBox="0 0 24 24" aria-hidden="true">
            <g fill="none" stroke="var(--brand-blue)" stroke-width="1.8">
              <circle cx="12" cy="12" r="10"/>
              <ellipse cx="12" cy="12" rx="4.5" ry="10"/>
              <path d="M2 12h20M4 7h16M4 17h16"/>
            </g>
          </svg>
          www.company.com
        </li>
      </ul>
    </div>
  </section>

  <section class="card card--back" aria-label="Business card back">
    <svg class="card__frame" viewBox="0 0 840 480" aria-hidden="true">
      <polygon points="440,54 800,40 800,162" fill="var(--brand-blue)"/>
      <rect x="40" y="40" width="380" height="18" fill="var(--white)"/>
      <rect x="40" y="40" width="18" height="236" fill="var(--white)"/>
      <rect x="782" y="180" width="18" height="260" fill="var(--white)"/>
      <rect x="500" y="422" width="300" height="18" fill="var(--white)"/>
    </svg>
    <h2 class="company-name">Sunridge Lighting Distributors</h2>
  </section>

</main>
</body>
</html>
```